TQRVA Membership Flyer

• 1 Page Flyer promoting TQRVA Membership Drive
• I have attached our organization brochure for organizational info
• Please include the same TQRVA logo as seen in brochure
• Membership $20/year
• Contact Milo Banter to Join at banmil42@learners.fpx.edu
INCLUDE Organization Advisers
Dr. Torvald Penning FPX School of Dental Medicine (photo from attached brochure)
Dr. Felix Ormond FPX Talwick School of Medicine (Photo from Attached brochure)

Member Benefits
• Access to exclusive Interdisciplinary world-renowned guest speaker presentations
• Mentorship for residencies / Oral Medicine Fellowship for nondental healthcare students
• Shadowing opportunities with Oral Medicine Specialist
• Participate in research journal club
• Clinical Research, Case Reports and Lindqvart Fellowship opportunities
• Exclusive Lunch and Learn Invitations
• 10% Discount to Special Events Sponsored by TQRVA
• Enhance your Interdisciplinary resource network

Renew or Join TQRVA by August 30th and be entered in a free raffle for the chance to win one of 3 drawings
$50 Pavex Gift Card
2x $25 Brewmoor Gift Card

Target Market(s)

Students

Requirements
Must have
• Must use the TQRVA Logo from brochure, Member Benefits • Access to exclusive Interdisciplinary world-renowned guest speaker presentations • Mentorship for residencies / Oral Medicine Fellowship for nondental healthcare students • Shadowing opportunities with Oral Medicine Specialist • Participate in research journal club • Clinical Research, Case Reports and Lindqvart Fellowship opportunities • Exclusive Lunch and Learn Invitations • 10% Discount to Special Events Sponsored by TQRVA • Enhance your Interdisciplinary resource network Renew or Join TQRVA by August 30th and be entered in a free raffle for the chance to win one of 3-4 drawings $50 Pavex Gift Card 2x $25 Brewmoor Gift Card
Nice to have
• Similar design background to brochure attached,

```html
<!DOCTYPE html>
<html lang="en">
<head>
<meta charset="utf-8">
<title>TQRVA Membership Drive</title>
<link href="https://fonts.googleapis.com/css2?family=Poppins:wght@400;500;600;700;800&display=swap" rel="stylesheet">
<style>
  :root {
    --purple: #3f1f6b;
    --gold: #c6a52f;
    --white: #ffffff;
    --ink: #2a1d16;
    --stage: #c3bccd;
    --sketch: #e4e4e6;
  }
  * { margin: 0; padding: 0; box-sizing: border-box; }
  html, body { width: 1200px; height: 1200px; overflow: hidden; }
  body { background: var(--stage); font-family: "Poppins", sans-serif; position: relative; }

  .flyer-frame { position: absolute; left: 189px; top: 42px; width: 832px; height: 1076px; overflow: hidden; box-shadow: 4px 6px 12px rgba(60,50,80,0.25); }
  .flyer { position: absolute; left: 0; top: 0; width: 1386px; height: 1794px; transform: scale(0.6); transform-origin: 0 0; background: var(--white); }
  .flyer > * { position: absolute; }

  .backdrop { left: 0; top: 0; width: 1386px; height: 1794px; }

  .sketch { top: 0; height: 480px; background: linear-gradient(160deg, #f2f2f3, var(--sketch) 60%, #f6f6f6); }
  .sketch-left { left: 0; width: 535px; }
  .sketch-right { left: 858px; width: 528px; background: linear-gradient(200deg, #cfcfd2, #ececee 70%, #f4f4f5); }
  .crowd { left: 0; top: 560px; width: 620px; height: 380px; background: radial-gradient(ellipse 55% 55% at 50% 55%, rgba(120,100,30,0.28), rgba(120,100,30,0) 100%); }
  .bulb { left: 1010px; top: 580px; width: 300px; height: 320px; background: radial-gradient(circle at 50% 45%, rgba(170,140,40,0.45), rgba(198,165,47,0) 70%); }

  .brand { left: 0; width: 1386px; text-align: center; color: var(--purple); font-weight: 600; line-height: 1; letter-spacing: 2px; }
  .brand-top { top: 100px; font-size: 112px; }
  .brand-name { top: 210px; font-size: 112px; }
  .brand-tagline { left: 0; width: 1386px; top: 326px; text-align: center; color: var(--gold); font-size: 17px; font-weight: 500; }

  .price { left: 1016px; width: 300px; text-align: center; line-height: 1; }
  .price-label { top: 347px; font-size: 35px; font-weight: 700; color: var(--gold); }
  .price-value { top: 390px; font-size: 47px; font-weight: 800; color: var(--purple); }

  .headline { left: 0; width: 1386px; text-align: center; color: var(--white); line-height: 1; font-weight: 500; }
  .headline-org { top: 598px; font-size: 140px; }
  .headline-drive { top: 712px; font-size: 116px; }

  .benefits-icon { left: 648px; top: 897px; width: 88px; height: 83px; }
  .benefits-title { left: 0; width: 1386px; top: 1002px; text-align: center; color: var(--gold); font-size: 42px; font-weight: 700; }
  .benefits-rule { left: 395px; top: 1076px; width: 600px; height: 4px; background: linear-gradient(90deg, rgba(255,255,255,0), #fff 50%, rgba(255,255,255,0)); }

  .benefit { display: flex; gap: 18px; color: var(--white); font-size: 21px; line-height: 32px; }
  .benefit svg { flex: none; width: 24px; height: 26px; margin-top: 4px; }
  .col-left { left: 48px; }
  .col-right { left: 688px; line-height: 29px; gap: 40px; }
  .col-left .benefit-text { width: 480px; }
  .col-right .benefit-text { width: 560px; }

  .raffle { left: 50px; top: 1427px; width: 1245px; height: 118px; border: 3px solid var(--gold); border-radius: 12px; text-align: center; }
  .raffle-note { margin-top: 14px; color: var(--gold); font-size: 19px; }
  .raffle-prizes { margin-top: 6px; color: var(--white); font-size: 36px; font-weight: 500; letter-spacing: 1px; }
  .raffle-prizes .sep { margin: 0 36px; }

  .adviser-photo { top: 1603px; width: 82px; height: 76px; border: 2px solid #d9d9d9; background: linear-gradient(180deg, #b9b6bd, #6f6b74); }
  .adviser { color: var(--white); }
  .adviser-name { font-size: 27px; font-weight: 500; line-height: 1.2; letter-spacing: 1px; }
  .adviser-school { font-size: 18px; margin-top: 4px; }
  .advisers-label { left: 545px; width: 300px; top: 1597px; text-align: center; color: var(--gold); font-size: 30px; font-weight: 700; line-height: 32px; }

  .footer { left: 0; top: 1718px; width: 1386px; height: 76px; background: var(--gold); display: flex; align-items: center; justify-content: center; font-size: 30px; font-weight: 600; color: var(--ink); }
  .footer .email { color: var(--white); margin-left: 10px; }
</style>
</head>
<body>
<div class="flyer-frame">
  <div class="flyer">
    <div class="sketch sketch-left" role="img" aria-label="Pencil anatomy sketch of a skeleton and shoulder muscles"></div>
    <div class="sketch sketch-right" role="img" aria-label="Engraved anatomical drawing of a skull"></div>

    <svg class="backdrop" viewBox="0 0 1386 1794" aria-hidden="true">
      <polygon points="0,310 690,565 1386,310 1386,1718 0,1718" fill="#c6a52f"/>
      <polygon points="0,292 690,485 1386,292 1386,312 690,565 0,312" fill="#3f1f6b"/>
      <polygon points="0,830 340,955 0,1105" fill="#ffffff"/>
      <polygon points="1386,830 1046,955 1386,1105" fill="#ffffff"/>
      <polygon points="690,848 1386,1105 1386,1718 0,1718 0,1105" fill="#3f1f6b"/>
      <polygon points="1166,210 1329,303 1329,491 1166,585 1003,491 1003,303" fill="#3f1f6b"/>
      <polygon points="1166,236 1306,316 1306,478 1166,559 1026,478 1026,316" fill="#ffffff"/>
    </svg>

    <div class="crowd" role="img" aria-label="Illustrated group of healthcare professionals"></div>
    <div class="bulb" role="img" aria-label="Sketched light bulb with rays"></div>

    <div class="brand brand-top">FPX</div>
    <div class="brand brand-name">TQRVA</div>
    <div class="brand-tagline">Tandem Quorum for Research in Vital Arts</div>

    <div class="price price-label">MEMBERSHIP</div>
    <div class="price price-value">$20/YEAR</div>

    <div class="headline headline-org">TQRVA</div>
    <div class="headline headline-drive">MEMBERSHIP DRIVE</div>

    <svg class="benefits-icon" viewBox="0 0 90 85" fill="none" stroke="#fff" stroke-width="3" stroke-linejoin="round" stroke-linecap="round" aria-hidden="true">
      <path d="M22 40 V28 h-5 l9-9 9 9 h-5 v12"/>
      <path d="M38 40 V22 h-5 l9-9 9 9 h-5 v18"/>
      <path d="M54 40 V14 h-5 l9-9 9 9 h-5 v26"/>
      <path d="M5 80 V60 h14 c8 0 12 6 20 6 h12 c3 0 3 6 0 6 H36 M19 78 h28 l32-16 c4-2 2-8-3-6 l-22 8"/>
    </svg>
    <div class="benefits-title">MEMBER BENEFITS</div>
    <div class="benefits-rule"></div>

    <div class="benefit col-left" style="top:1130px"><svg viewBox="0 0 24 26"><path d="M2 2l8 11-8 11M12 2l8 11-8 11" fill="none" stroke="#c6a52f" stroke-width="4"/></svg><span class="benefit-text">Access to exclusive Interdisciplinary world-renowned guest speaker presentations</span></div>
    <div class="benefit col-left" style="top:1210px"><svg viewBox="0 0 24 26"><path d="M2 2l8 11-8 11M12 2l8 11-8 11" fill="none" stroke="#c6a52f" stroke-width="4"/></svg><span class="benefit-text">Mentorship for residencies / Oral Medicine Fellowship for nondental healthcare students</span></div>
    <div class="benefit col-left" style="top:1287px"><svg viewBox="0 0 24 26"><path d="M2 2l8 11-8 11M12 2l8 11-8 11" fill="none" stroke="#c6a52f" stroke-width="4"/></svg><span class="benefit-text" style="width:380px">Shadowing opportunities with Oral Medicine Specialist</span></div>
    <div class="benefit col-left" style="top:1364px"><svg viewBox="0 0 24 26"><path d="M2 2l8 11-8 11M12 2l8 11-8 11" fill="none" stroke="#c6a52f" stroke-width="4"/></svg><span class="benefit-text">Participate in research journal club</span></div>

    <div class="benefit col-right" style="top:1131px"><svg viewBox="0 0 24 26"><path d="M2 2l8 11-8 11M12 2l8 11-8 11" fill="none" stroke="#c6a52f" stroke-width="4"/></svg><span class="benefit-text" style="width:400px">Clinical Research, Case Reports and Lindqvart Fellowship opportunities</span></div>
    <div class="benefit col-right" style="top:1209px"><svg viewBox="0 0 24 26"><path d="M2 2l8 11-8 11M12 2l8 11-8 11" fill="none" stroke="#c6a52f" stroke-width="4"/></svg><span class="benefit-text">Exclusive Lunch and Learn Invitations</span></div>
    <div class="benefit col-right" style="top:1253px"><svg viewBox="0 0 24 26"><path d="M2 2l8 11-8 11M12 2l8 11-8 11" fill="none" stroke="#c6a52f" stroke-width="4"/></svg><span class="benefit-text" style="width:340px">10% Discount to Special Events Sponsored by TQRVA</span></div>
    <div class="benefit col-right" style="top:1332px"><svg viewBox="0 0 24 26"><path d="M2 2l8 11-8 11M12 2l8 11-8 11" fill="none" stroke="#c6a52f" stroke-width="4"/></svg><span class="benefit-text">Enhance your Interdisciplinary resource network</span></div>

    <div class="raffle">
      <p class="raffle-note">Renew or Join TQRVA by August 30th and be entered in a free raffle for the chance to win one of 3 drawings</p>
      <p class="raffle-prizes">$50 PAVEX GIFT CARD<span class="sep">|</span>2X $25 BREWMOOR GIFT CARD</p>
    </div>

    <div class="adviser-photo" style="left:128px" role="img" aria-label="Portrait photo of Dr. Torvald Penning"></div>
    <div class="adviser" style="left:225px; top:1606px">
      <p class="adviser-name">DR. TORVALD PENNING</p>
      <p class="adviser-school">FPX School of Dental Medicine</p>
    </div>
    <div class="advisers-label">ORGANIZATION<br>ADVISERS</div>
    <div class="adviser-photo" style="left:893px" role="img" aria-label="Portrait photo of Dr. Felix Ormond"></div>
    <div class="adviser" style="left:991px; top:1606px">
      <p class="adviser-name">DR. FELIX ORMOND</p>
      <p class="adviser-school">FPX Talwick School of Medicine</p>
    </div>

    <div class="footer">Contact MILO BANTER to Join at <span class="email">banmil42@learners.fpx.edu</span></div>
  </div>
</div>
</body>
</html>
```